FLyer for Malaysia's No. 1 Healthcare Job Site (name of job site: Vireta)

Objective of flyer - to get people to register on the job site
Must have:
Logo and Name (Vireta)
Tagline: Malaysia's #1 Healthcare Job site
url: www.vireta-jobs.example
social media links
FB:Vireta
LinkedIn: viretajobs
Instagram: @viretajobs

WE cover the entire healthcare industry areas (doctors, nurses, dentists, pharmacists, psychologists, administrative staff, biomedical engineers....etc)

Please remember that our focus service is our Job-site, we want people to realize in the first look that we are a healthcare Job site.

Flyer size: A5

Color code: #279582 (80%) & #96c836 (20%)

Target Market(s)

All Healthcare Professionals in Malaysia

Industry/Entity Type

Healthcare

Requirements
Must have
• Web site: www.vireta-jobs.example
• Logo and Tagline (attached)
• 2 side design
• Really important (Our Product is our Job site)
Nice to have
• Asian Healthcare professionals, info graphic icons.

```html
<!DOCTYPE html>
<html lang="en">
<head>
<meta charset="utf-8">
<title>Welcome to Vireta</title>
<link rel="stylesheet" href="https://fonts.googleapis.com/css2?family=Lato:wght@400;700&display=swap">
<style>
  :root {
    --teal: #2c9a9e;
    --teal-dark: #2a9094;
    --green: #7cb83c;
    --ink: #1c1c1c;
    --band-grey: #a7a7a7;
    --white: #ffffff;
  }
  * { margin: 0; padding: 0; box-sizing: border-box; }
  html, body { width: 1200px; height: 846px; overflow: hidden; background: var(--white); }
  .flyer {
    position: relative;
    width: 1200px;
    height: 846px;
    font-family: "Lato", Arial, sans-serif;
    color: var(--ink);
    background: var(--white);
  }
  .headline {
    position: absolute;
    top: 52px; left: 0; width: 100%;
    text-align: center;
    font-size: 70px;
    font-weight: 700;
    letter-spacing: 1px;
    color: var(--teal);
  }
  .intro {
    position: absolute;
    left: 75px; width: 1051px;
    font-size: 22.5px;
    line-height: 29px;
    letter-spacing: 0.4px;
    text-align: justify;
    text-align-last: left;
  }
  .intro--lead { top: 164px; }
  .intro--services { top: 251px; }
  .highlight { color: var(--green); }
  .audience {
    position: absolute;
    left: 0; width: 100%;
    text-align: center;
    font-size: 22.5px;
    line-height: 29px;
    letter-spacing: 0.4px;
  }
  .audience--seekers { top: 399px; }
  .audience--employers { top: 486px; }
  .audience__title {
    color: var(--teal);
    font-weight: 700;
    letter-spacing: 1px;
  }
  .career-band {
    position: absolute;
    top: 586px; left: 0;
    width: 100%; height: 93px;
    background: var(--band-grey);
    color: var(--white);
    text-align: center;
    font-size: 22.5px;
    line-height: 29px;
    letter-spacing: 0.5px;
    padding-top: 17px;
  }
  .contact {
    position: absolute;
    top: 708px; left: 0;
    width: 100%; height: 138px;
    background: var(--teal);
    color: var(--white);
  }
  .contact__title {
    position: absolute;
    top: 22px; left: 0; width: 100%;
    text-align: center;
    font-size: 23px;
    letter-spacing: 0.6px;
  }
  .contact__rule {
    position: absolute;
    top: 50px; left: 440px;
    width: 320px; height: 1px;
    background: linear-gradient(90deg, rgba(255,255,255,0), rgba(255,255,255,0.6), rgba(255,255,255,0));
  }
  .channel {
    position: absolute;
    top: 70px;
    display: flex;
    align-items: center;
    gap: 10px;
    font-size: 20px;
    font-weight: 700;
    letter-spacing: 0.3px;
  }
  .channel svg { width: 38px; height: 38px; flex: none; }
  .channel--web { left: 167px; }
  .channel--page { left: 407px; }
  .channel--photo { left: 649px; }
  .channel--posts { left: 891px; }
</style>
</head>
<body>
<main class="flyer">
  <h1 class="headline">Welcome to VIRETA!</h1>

  <p class="intro intro--lead">We are <span class="highlight">Malaysia’s #1 Healthcare Job Site</span> fully dedicated to the healthcare industry, being a part of the new generation of Job Sites worldwide.</p>

  <p class="intro intro--services">Our jobs cover niche Healthcare Vacancies - connecting the you to the right employers. Use VIRETA to create your CV, search for specific jobs, survey market salary ranges and most importantly, gain access to a growing network of local and international Healthcare Employers.</p>

  <section class="audience audience--seekers">
    <h2 class="audience__title">JOBSEEKERS</h2>
    <p>In just 3 easy&nbsp; steps, find your dream Healthcare job!</p>
  </section>

  <section class="audience audience--employers">
    <h2 class="audience__title">EMPLOYERS</h2>
    <p>We’ve made Talent Recruitment more convenient and time efficient for you.</p>
  </section>

  <section class="career-band">
    <p>Are you a Doctor? A Nurse? A Pharmacist? A Medical Sales Rep?</p>
    <p>If you’re interested in a Healthcare Job – We’re here to you grow your CAREER!</p>
  </section>

  <footer class="contact">
    <h2 class="contact__title">Get In Touch With Us!</h2>
    <div class="contact__rule"></div>

    <div class="channel channel--web">
      <svg viewBox="0 0 40 40" fill="none" stroke="#fff" stroke-width="2.2" aria-hidden="true">
        <circle cx="20" cy="20" r="17"/>
        <ellipse cx="20" cy="20" rx="7.5" ry="17"/>
        <line x1="20" y1="3" x2="20" y2="37"/>
        <line x1="3" y1="20" x2="37" y2="20"/>
        <path d="M6 11h28M6 29h28"/>
      </svg>
      <span>vireta-jobs.example</span>
    </div>

    <div class="channel channel--page">
      <svg viewBox="0 0 40 40" fill="none" stroke="#fff" stroke-width="2.2" aria-hidden="true">
        <circle cx="20" cy="20" r="17"/>
      </svg>
      <span>/viretajobs</span>
    </div>

    <div class="channel channel--photo">
      <svg viewBox="0 0 40 40" fill="none" stroke="#fff" stroke-width="2.2" aria-hidden="true">
        <circle cx="20" cy="20" r="17"/>
      </svg>
      <span>/viretajobs</span>
    </div>

    <div class="channel channel--posts">
      <svg viewBox="0 0 40 40" fill="none" stroke="#fff" stroke-width="2.2" aria-hidden="true">
        <circle cx="20" cy="20" r="17"/>
      </svg>
      <span>/viretajobs</span>
    </div>
  </footer>
</main>
</body>
</html>
```